Website Design for Car Donations

Revise current site www.ridesforhonor.org

Sites i like:

https://www.wheelsformilitary.org

https://autogivingforheroes.org

https://plinkmock.com/144490c6/screen/39053423

Coding

Coded - Design and coding required

Number of Pages Required

1 page

```html
<!DOCTYPE html>
<html lang="en">
<head>
<meta charset="utf-8">
<title>Rides For Honor — Donate Your Car</title>
<link rel="stylesheet" href="https://fonts.googleapis.com/css2?family=Roboto:wght@400;500;700;900&display=swap">
<style>
:root{
  --red:#d0121b;
  --red-dark:#a80d14;
  --navy:#0b2a86;
  --navy-deep:#061d63;
  --field:#07185a;
  --ink:#222;
  --muted:#555;
  --light:#f3f3f3;
  --footer:#1f1f1f;
  --white:#fff;
}
*{box-sizing:border-box;margin:0;padding:0}
html,body{width:1200px;height:3390px;overflow:hidden}
body{font-family:'Roboto',Arial,sans-serif;color:var(--ink);background:var(--white);position:relative}
.abs{position:absolute}

/* header */
.site-header{position:absolute;top:0;left:0;width:1200px;height:151px;background:var(--white)}
.brand{position:absolute;left:80px;top:56px;display:flex;align-items:center;gap:12px}
.brand-mark{width:30px;height:30px;background:var(--red);border-radius:50%}
.brand-name{font-size:26px;font-weight:700;color:var(--red);letter-spacing:.5px;text-transform:uppercase}
.top-phone{position:absolute;right:72px;top:28px;font-size:19px;color:var(--ink);display:flex;align-items:center;gap:10px}
.main-nav{position:absolute;right:72px;top:78px;display:flex;align-items:center;gap:32px;font-size:15px;font-weight:500;text-transform:uppercase}
.main-nav a{color:var(--ink);text-decoration:none;height:68px;display:flex;align-items:center}
.main-nav a.active{color:var(--red);border-bottom:5px solid var(--red);padding-top:5px}
.main-nav .btn-donate{background:var(--red);color:var(--white);height:38px;padding:0 22px;border-radius:4px;font-weight:700}

/* hero */
.hero{position:absolute;top:151px;left:0;width:1200px;height:622px;
  background:linear-gradient(110deg,#6f6a4c 0%,#a99a73 35%,#8a7a5d 55%,#5b4a36 80%,#3d3427 100%)}

/* donate intro */
.donate-intro{position:absolute;top:773px;left:0;width:1200px;height:599px;background:var(--light)}
.donate-intro h1{position:absolute;left:120px;top:140px;font-size:29px;font-weight:500;letter-spacing:1.5px;text-transform:uppercase}
.donate-intro .kicker{position:absolute;left:120px;top:186px;font-size:15px;font-weight:500;letter-spacing:.8px;text-transform:uppercase}
.perk{position:absolute;width:210px;text-align:center;font-size:14px;line-height:18px;text-transform:uppercase;color:#333}
.perk svg{display:block;margin:0 auto 10px}

.donate-form{position:absolute;left:687px;top:81px;width:398px;height:468px;background:var(--navy);border:2px solid #1c3fa8}
.form-ribbon{position:absolute;left:-27px;top:31px;width:450px;height:62px;background:var(--red);color:var(--white);
  font-size:27px;font-weight:500;text-align:center;line-height:62px;text-transform:uppercase;letter-spacing:.5px}
.form-badge{position:absolute;left:168px;top:-12px;width:62px;height:44px;background:var(--red);border-radius:31px 31px 0 0;display:flex;justify-content:center;padding-top:8px}
.form-sub{position:absolute;top:108px;width:100%;text-align:center;color:var(--white);font-size:17px;font-weight:500}
.field{position:absolute;left:30px;width:336px;height:34px;background:var(--field);border-radius:4px;color:#cdd6f5;font-size:12px;padding:0 16px;line-height:34px}
.field.half{width:162px}
.field.half::after{content:"";position:absolute;right:12px;top:14px;border:6px solid transparent;border-top-color:#fff}
.form-submit{position:absolute;left:127px;top:412px;width:145px;height:34px;background:var(--red);color:var(--white);
  border-radius:3px;font-size:13px;font-weight:700;text-align:center;line-height:34px;text-transform:uppercase}

/* how */
.how{position:absolute;top:1372px;left:0;width:1200px;height:420px;background:var(--white)}
.section-title{position:absolute;width:100%;text-align:center;font-size:28px;font-weight:500;letter-spacing:1.5px;text-transform:uppercase}
.step{position:absolute;top:150px;width:320px;text-align:center}
.step svg{display:block;margin:0 auto 18px}
.step h3{font-size:15px;font-weight:500;text-transform:uppercase;line-height:20px;letter-spacing:.3px}
.step p{font-size:14px;line-height:18px;color:var(--muted);margin-top:10px;padding:0 30px}

/* why */
.why{position:absolute;top:1792px;left:0;width:1200px;height:576px;
  background:linear-gradient(90deg,var(--navy-deep) 0%,var(--navy) 60%,#0e32a0 100%);color:var(--white)}
.why h2{position:absolute;left:120px;top:90px;font-size:30px;font-weight:500;letter-spacing:1.2px;text-transform:uppercase}
.why .lead{position:absolute;left:120px;top:136px;width:440px;font-size:15px;font-weight:700;line-height:21px}
.why ul{position:absolute;left:120px;top:200px;width:450px;list-style:none}
.why li{position:relative;padding-left:22px;font-size:15px;line-height:20px;margin-bottom:19px}
.why li::before{content:"";position:absolute;left:0;top:6px;width:9px;height:9px;background:var(--white);border-radius:50%}
.why li b{font-weight:700}
.why-photo{position:absolute;left:601px;top:97px;width:527px;height:315px;
  background:linear-gradient(180deg,#a9c9e8 0%,#c5d8ea 45%,#8c8a6a 75%,#6c6a50 100%)}

/* faq */
.faq{position:absolute;top:2368px;left:0;width:1200px;height:649px;background:var(--white)}
.faq-list{position:absolute;left:120px;top:170px;width:513px;list-style:none}
.faq-list li{position:relative;height:34px;background:#f1f1f1;margin-bottom:9px;font-size:15px;line-height:34px;padding:0 14px;color:#333}
.faq-list li::after{content:"";position:absolute;right:12px;top:14px;border:5px solid transparent;border-top-color:#333}
.faq-map{position:absolute;left:667px;top:152px;width:497px;height:339px;
  background:linear-gradient(135deg,#3c3b6e 0%,#6a6a95 28%,#ecebeb 50%,#c43a45 75%,#9e1b28 100%);
  border-radius:40px 90px 30px 120px}

/* footer */
.site-footer{position:absolute;top:3017px;left:0;width:1200px;height:323px;background:var(--footer);color:var(--white)}
.footer-brand{position:absolute;left:80px;top:72px;display:flex;align-items:center;gap:10px}
.footer-brand .brand-name{font-size:22px}
.footer-about{position:absolute;left:120px;top:135px;width:310px;font-size:13px;line-height:17px;color:#eee}
.footer-col{position:absolute;top:78px}
.footer-col h4{font-size:15px;font-weight:700;letter-spacing:.8px;text-transform:uppercase;margin-bottom:28px}
.footer-col a{display:block;color:var(--white);text-decoration:none;font-size:13px;letter-spacing:.6px;text-transform:uppercase;margin-bottom:14px}
.badge-shape{width:100px;height:38px;background:#f0f0f0;border-radius:4px;margin:0 0 16px 14px}
.badge-round{width:60px;height:34px;background:#dfe7ef;border-radius:50%;margin-left:34px}
.call-col{text-align:center;width:236px}
.call-col .phone-circle{width:40px;height:40px;border:2px solid var(--white);border-radius:50%;margin:0 auto 14px;display:flex;align-items:center;justify-content:center}
.call-col .big-phone{font-size:27px;font-weight:700}
.call-col small{display:block;font-size:12px;font-weight:700;line-height:15px;margin-top:6px}

.bottom-bar{position:absolute;top:3340px;left:0;width:1200px;height:50px;background:var(--red-dark);color:var(--white)}
.bottom-bar p{position:absolute;left:120px;top:17px;font-size:14px;font-weight:700}
.social{position:absolute;right:82px;top:14px;display:flex;gap:12px}
.social span{width:22px;height:22px;background:#1a1a1a;border-radius:50%}
</style>
</head>
<body>

<header class="site-header">
  <div class="brand"><span class="brand-mark"></span><span class="brand-name">Rides For Honor</span></div>
  <div class="top-phone">
    <svg width="22" height="22" viewBox="0 0 24 24"><circle cx="12" cy="12" r="11" fill="none" stroke="#d0121b" stroke-width="2"/><path d="M8 6l2 0 1 3-1.5 1a7 7 0 0 0 4 4l1-1.5 3 1v2c0 1-1 1.5-2 1.5A10 10 0 0 1 6.5 8C6.5 7 7 6 8 6z" fill="#d0121b"/></svg>
    1-800-555-0142
  </div>
  <nav class="main-nav">
    <a class="active" href="#how">How to Donate</a>
    <a href="#why">Why Donate</a>
    <a href="#faq">FAQ</a>
    <a href="#about">About</a>
    <a class="btn-donate" href="#donate">Donate Now</a>
  </nav>
</header>

<section class="hero" role="img" aria-label="Military family in camouflage uniforms embracing their young son, who holds an American flag"></section>

<section class="donate-intro" id="donate">
  <h1>Donate Your Car to Veterans</h1>
  <p class="kicker">Make a Difference</p>

  <div class="perk" style="left:71px;top:240px">
    <svg width="50" height="50" viewBox="0 0 50 50" fill="none" stroke="#d0121b" stroke-width="3"><circle cx="12" cy="36" r="7"/><circle cx="22" cy="42" r="6"/><path d="M17 31L40 6M26 37L44 18"/><rect x="28" y="6" width="18" height="24" rx="2" transform="rotate(20 37 18)"/></svg>
    You have no<br>costs
  </div>
  <div class="perk" style="left:257px;top:240px">
    <svg width="80" height="50" viewBox="0 0 80 50" fill="#d0121b"><rect x="4" y="22" width="46" height="16" rx="2"/><path d="M50 14h14l10 12v12H50z"/><circle cx="18" cy="42" r="6" fill="#fff" stroke="#d0121b" stroke-width="3"/><circle cx="62" cy="42" r="6" fill="#fff" stroke="#d0121b" stroke-width="3"/><path d="M14 22L34 4l4 4" stroke="#d0121b" stroke-width="3" fill="none"/></svg>
    Free towing,<br>running or not
  </div>
  <div class="perk" style="left:449px;top:240px">
    <svg width="50" height="50" viewBox="0 0 50 50"><rect x="6" y="18" width="38" height="28" fill="#d0121b"/><rect x="12" y="4" width="26" height="24" fill="#fff" stroke="#d0121b" stroke-width="3"/><text x="25" y="22" font-size="14" font-weight="700" fill="#d0121b" text-anchor="middle" font-family="Roboto,sans-serif">$</text><path d="M6 18l19 16 19-16" stroke="#fff" stroke-width="2" fill="none"/></svg>
    We issue you an<br>IRS tax receipt
  </div>
  <div class="perk" style="left:71px;top:374px">
    <svg width="50" height="50" viewBox="0 0 50 50" fill="none" stroke="#d0121b" stroke-width="3"><rect x="8" y="4" width="30" height="40" rx="2"/><path d="M14 14h18M14 22h10M14 30h8"/><circle cx="34" cy="32" r="8" fill="#fff"/><path d="M40 38l6 6"/></svg>
    We take care of<br>all paperwork
  </div>
  <div class="perk" style="left:257px;top:374px">
    <svg width="70" height="50" viewBox="0 0 70 50"><path d="M8 28l8-14h30l10 14h6v12H4V28z" fill="#d0121b"/><circle cx="18" cy="40" r="6" fill="#fff" stroke="#d0121b" stroke-width="3"/><circle cx="50" cy="40" r="6" fill="#fff" stroke="#d0121b" stroke-width="3"/><path d="M30 26l8 8 22-26" stroke="#fff" stroke-width="7" fill="none"/><path d="M30 26l8 8 22-26" stroke="#d0121b" stroke-width="4" fill="none"/></svg>
    No DMV<br>hassles
  </div>
  <div class="perk" style="left:449px;top:374px">
    <svg width="60" height="50" viewBox="0 0 60 50" fill="none" stroke="#d0121b" stroke-width="3"><rect x="4" y="10" width="52" height="30" rx="2"/><path d="M4 16h52" stroke-dasharray="3 3"/><path d="M14 32l5-8h22l5 8v4H14z" fill="#d0121b"/></svg>
    Vacation<br>voucher
  </div>

  <form class="donate-form" aria-label="Donate your car online">
    <div class="form-badge"><svg width="30" height="20" viewBox="0 0 30 20" fill="#fff"><path d="M4 10l4-7h14l4 7h2v6H2v-6z"/><circle cx="9" cy="16" r="3" fill="#d0121b"/><circle cx="21" cy="16" r="3" fill="#d0121b"/></svg></div>
    <div class="form-ribbon">Donate Your Car Online</div>
    <p class="form-sub">Full Tax Deduction - Running or Not</p>
    <div class="field" style="top:143px">First Name</div>
    <div class="field" style="top:187px">Phone</div>
    <div class="field" style="top:230px">Email</div>
    <div class="field" style="top:273px">Zip Code</div>
    <div class="field half" style="top:316px">Choose Year</div>
    <div class="field half" style="top:316px;left:204px">Choose Make</div>
    <div class="field" style="top:360px">Vehicle Model</div>
    <div class="form-submit">Donate Now</div>
  </form>
</section>

<section class="how" id="how">
  <h2 class="section-title" style="top:78px">How to Donate</h2>
  <div class="step" style="left:66px">
    <svg width="70" height="60" viewBox="0 0 70 60"><path d="M6 18c0-8 58-8 58 0v6H50v-6H20v6H6z" fill="#d0121b"/><path d="M16 26h38l8 28H8z" fill="#d0121b"/><circle cx="35" cy="40" r="8" fill="#fff"/><circle cx="35" cy="40" r="3" fill="#d0121b"/></svg>
    <h3>Call us at 1-800-555-0142 or<br>fill out the online form</h3>
    <p>Donating your vehicle is easy and donation is accepted nationwide.</p>
  </div>
  <div class="step" style="left:450px">
    <svg width="100" height="60" viewBox="0 0 100 60"><rect x="4" y="30" width="50" height="16" fill="#d0121b"/><path d="M54 20h18l12 14v12H54z" fill="#d0121b"/><path d="M60 24h10l7 9H60z" fill="#fff"/><path d="M10 30L40 6l6 6M40 6v10" stroke="#333" stroke-width="3" fill="none"/><circle cx="20" cy="50" r="7" fill="#333"/><circle cx="72" cy="50" r="7" fill="#333"/></svg>
    <h3>We tow the vehicle</h3>
    <p>Any vehicles are accepted and we will arrange to pick up your vehicle when it is most convenient for you.</p>
  </div>
  <div class="step" style="left:839px">
    <svg width="60" height="70" viewBox="0 0 60 70" fill="none" stroke="#d0121b" stroke-width="3"><rect x="8" y="8" width="44" height="58" rx="2"/><rect x="20" y="2" width="20" height="10" rx="2" fill="#fff"/><path d="M16 26l4 4 6-8M32 26h14M16 42l4 4 6-8M32 42h14" stroke="#0b2a86"/></svg>
    <h3>Tax Write-Off</h3>
    <p>Once the vehicle donation is complete, you will receive your tax deductable vehicle donation receipt.</p>
  </div>
</section>

<section class="why" id="why">
  <h2>Why Donate Your Car to Us</h2>
  <p class="lead">IRS 501(c)3 Approved : Free 24/7 Pickup with No DMV Hassles.</p>
  <ul>
    <li><b>Free Local Towing :</b> We will pick up your car donation, running or not, when it's most convenient, at home or work.</li>
    <li><b>Income Tax Deduction :</b> We issue you an IRS tax receipt and get you the highest tax write-off possible.</li>
    <li><b>No Paperwork Hassles :</b> We handle everything: DMV and IRS paperwork.</li>
    <li><b>Car donations help fund programs :</b> And benefit Valor Path Foundation. An IRS 501(c)3 nonprofit organization.</li>
    <li><b>Schedule a Free Pickup :</b> Complete the form and a representative will call you to arrange a convenient time to pickup your car.</li>
  </ul>
  <div class="why-photo" role="img" aria-label="Two soldiers in camouflage uniforms smiling beside a little girl holding a small American flag, blue sky behind"></div>
</section>

<section class="faq" id="faq">
  <h2 class="section-title" style="top:58px">Frequently Asked Questions</h2>
  <ul class="faq-list">
    <li>What types of vehicles can be donated?</li>
    <li>What paperwork do I need to donate my vehicle?</li>
    <li>Is my donated vehicle tax-deductible?</li>
    <li>What if the vehicle is not registered in my name?</li>
    <li>How much will I receive as a tax deduction for my vehicle?</li>
    <li>When will I receive my tax receipt?</li>
    <li>How do I schedule a pick up?</li>
  </ul>
  <div class="faq-map" role="img" aria-label="Map of the United States filled with the American flag"></div>
</section>

<footer class="site-footer" id="about">
  <div class="footer-brand"><span class="brand-mark"></span><span class="brand-name">Rides For Honor</span></div>
  <p class="footer-about">Car donations help fund programs and benefit Valor Path Foundation. An IRS 501(c)3 nonprofit organization. Schedule a Free Pickup: Complete the form and a representative will call you to arrange a convenient time to pickup your car.</p>
  <div class="footer-col" style="left:536px">
    <h4>Navigation</h4>
    <a href="#how">How to Donate</a>
    <a href="#why">Why Donate</a>
    <a href="#faq">FAQ</a>
    <a href="#about">About</a>
  </div>
  <div class="footer-col" style="left:700px">
    <h4>Safe &amp; Secure</h4>
    <div class="badge-shape"></div>
    <div class="badge-round"></div>
  </div>
  <div class="footer-col call-col" style="left:908px">
    <h4>Call Today to Donate</h4>
    <div class="phone-circle"><svg width="20" height="20" viewBox="0 0 24 24"><path d="M6 3l3 0 1.5 4-2 1.5a10 10 0 0 0 6 6l1.5-2 4 1.5v3c0 1.5-1.5 2-3 2A16 16 0 0 1 4 6c0-1.5.5-3 2-3z" fill="#fff"/></svg></div>
    <div class="big-phone">1-800-555-0142</div>
    <small>Live Operators Available<br>7 Days A Week</small>
  </div>
</footer>

<div class="bottom-bar">
  <p>Copyright © 2018 RIDES FOR HONOR. All Rights Reserved.</p>
  <div class="social"><span></span><span></span><span></span><span></span><span></span></div>
</div>

</body>
</html>
```